HiItsJonBrell.com needs a modern, eye-catching business card design

My name is Jon Brell and I own a video training (software development industry) website. I need a business card design that is eye catching for when I travel to conferences or do seminars. I would prefer something simple but bold. Something along the lines of this: https://pixvaultstatic.example/gallery_img/530172/44018/44018_9917302_530172_image.jpg

Note that I do not have a specific logo, but I do have an caricature I use on my site of myself. I've not attached it because I'm not really a fan of having it on my business cards. I would prefer lettering instead of an image. You can go to my website (https://hiitsjonbrell.com) for inspiration.

I want to add the following information on my card (the order of these, their size, and their casing is up to you):

Jon Brell
jon@HiItsJonBrell.com
@HiItsJonBrell
HiItsJonBrell.com
vidsharehub.example/HiItsJonBrell

I would also like to have somewhere on the card a small ad that says "Get a free course at https://HiItsJonBrell.com/FreeCourse". Feel free to play with that wording or layout if you need. I would prefer this text to be at the bottom of the card and subtle. Some small eye-catching thing might be ok but nothing huge or garish.

I plan on printing this card at pressquill.example (https://www.pressquill.example/us/design-guidelines/business-cards.html). I would like it to be the standard size (3.66" x 2.16"). I would prefer rounded corners and horizontal orientation. This is a two-side design. I would prefer the side with all of the information be primarily white but I like color text (again, flexible on that). On the front side, I like simple. Maybe just HiItsJonBrell.com (casing on that is up to you - whatever looks and reads the best - that goes for all of the casing). As for font choices, I prefer a modern, clean font. For example, Open Sans Light can be a nice option.

Website Info (might be helpful for the card):
Color Palette

Darkest blue - #263246
Alternate blue - #2F4E6A
Light blue - #2A98C3
Orange - #FF6201
White - #FFFFFF

Font for Jon Brell Logo

Jellyka Estryas Handwriting
http://www.typecrate.example/jellyka_estryas_handwriting.font

Fonts for Site Content and VidShare Thumbnails

Lovelo (bold title font)
http://www.glyphmill.example/lovelo-font/

Open Sans (body font)
http://www.letterbarn.example/fonts/open-sans

Industry/Entity Type

Software Development

Contact Information for Business Card

Jon Brell
jon@HiItsJonBrell.com
@HiItsJonBrell
HiItsJonBrell.com
vidsharehub.example/HiItsJonBrell

Get a free course at https://HiItsJonBrell.com/FreeCourse

Colors

Designer to choose colors to be used in the design.

Requirements
Nice to have
• Modern color - maybe primarily a color on the front and then that color as an accent on the back.
Should not have
• Lots of colors - I LOVE color but do not want a rainbow of colors on the card.

```html
<!DOCTYPE html>
<html lang="en">
<head>
<meta charset="utf-8">
<title>HiItsJonBrell.com Business Card</title>
<link rel="stylesheet" href="https://fonts.googleapis.com/css2?family=Open+Sans:wght@400;600;700&family=Oswald:wght@500&display=swap">
<style>
  :root {
    --backdrop: #ecebe8;
    --card: #3b3b3c;
    --accent: #2A98C3;
    --white: #ffffff;
    --muted: #d9d9d9;
  }
  * { margin: 0; padding: 0; box-sizing: border-box; }
  html, body { width: 1200px; height: 1000px; overflow: hidden; }
  body {
    background: var(--backdrop);
    position: relative;
    font-family: "Open Sans", Arial, sans-serif;
    color: var(--white);
  }
  .card {
    position: absolute;
    left: 267px;
    width: 665px;
    height: 395px;
    background: var(--card);
    border-radius: 30px;
    box-shadow: 0 6px 18px rgba(0,0,0,0.18);
  }
  .card--front { top: 75px; }
  .card--back { top: 535px; }

  /* Front */
  .brand {
    position: absolute;
    left: 0; right: 0; top: 150px;
    display: flex;
    align-items: center;
    justify-content: center;
    gap: 18px;
  }
  .brand__dot {
    width: 28px; height: 28px;
    border-radius: 50%;
    background: var(--accent);
  }
  .brand__name {
    font-size: 58px;
    font-weight: 600;
    letter-spacing: -0.5px;
    color: var(--white);
  }
  .promo {
    position: absolute;
    left: 0; right: 0; top: 347px;
    text-align: center;
    font-size: 16px;
    font-weight: 400;
  }
  .promo strong { font-weight: 700; }

  /* Back */
  .identity {
    position: absolute;
    right: 392px;
    top: 163px;
    text-align: right;
  }
  .identity__name {
    font-family: "Oswald", "Arial Narrow", sans-serif;
    font-weight: 500;
    font-size: 38px;
    line-height: 40px;
    color: var(--accent);
    letter-spacing: 0.5px;
    text-transform: uppercase;
  }
  .identity__role {
    font-size: 15px;
    color: var(--muted);
    margin-top: 4px;
  }
  .divider {
    position: absolute;
    left: 290px;
    top: 167px;
    width: 2px;
    height: 63px;
    background: var(--accent);
  }
  .contacts {
    position: absolute;
    left: 307px;
    top: 160px;
    list-style: none;
  }
  .contacts li {
    display: flex;
    align-items: center;
    gap: 7px;
    height: 24.5px;
    font-size: 16.5px;
  }
  .contacts svg { width: 15px; height: 15px; flex: none; }
  .social {
    position: absolute;
    left: 0; right: 0; top: 342px;
    display: flex;
    justify-content: center;
    align-items: center;
    gap: 8px;
    font-size: 16px;
    font-weight: 600;
  }
  .social__dot {
    width: 17px; height: 17px;
    border-radius: 50%;
    background: var(--accent);
  }
</style>
</head>
<body>
  <section class="card card--front">
    <div class="brand">
      <span class="brand__dot"></span>
      <span class="brand__name">HiItsJonBrell.com</span>
    </div>
    <p class="promo"><strong>Get a free course at</strong> https://HiItsJonBrell.com/FreeCourse</p>
  </section>

  <section class="card card--back">
    <div class="identity">
      <div class="identity__name">Jon Brell</div>
      <div class="identity__role">Owner / CEO</div>
    </div>
    <div class="divider"></div>
    <ul class="contacts">
      <li>
        <svg viewBox="0 0 16 16" aria-hidden="true"><rect x="1" y="3" width="14" height="10" rx="1" fill="#2A98C3"/><path d="M1.5 3.5 8 9l6.5-5.5" fill="none" stroke="#3b3b3c" stroke-width="1.4"/></svg>
        jon@HiItsJonBrell.com
      </li>
      <li>
        <svg viewBox="0 0 16 16" aria-hidden="true"><circle cx="8" cy="8" r="6.5" fill="none" stroke="#2A98C3" stroke-width="1.5"/><ellipse cx="8" cy="8" rx="2.8" ry="6.5" fill="none" stroke="#2A98C3" stroke-width="1.2"/><line x1="1.5" y1="8" x2="14.5" y2="8" stroke="#2A98C3" stroke-width="1.2"/></svg>
        HiItsJonBrell.com
      </li>
      <li>
        <svg viewBox="0 0 16 16" aria-hidden="true"><rect x="1.5" y="3" width="13" height="10" rx="2.5" fill="#2A98C3"/></svg>
        vidsharehub.example/HiItsJonBrell
      </li>
    </ul>
    <div class="social">
      <span class="social__dot"></span>
      <span>@HiItsJonBrell</span>
    </div>
  </section>
</body>
</html>
```